Summit Grading a Builders LLC business card

My current business card is very plain. it has my logo and contact information. I woud like something that stands out from the rest. please take a look at my website to see about my company.

Compayt Name - Summit Grading And Builders
Owner - Martin Kowalczyk
Business Address
Business Website - www.summitgradingandbuilders.example
Email - Summitgradingandbuilders@mailbox.example
Phone - 555-214-7390
Fax - 555-806-3127

Target Market(s)

Everyone age tang is 18 - 85

Industry/Entity Type

Business

Contact Information for Business Card

Nice and professional all in one.

Font styles to use
Serif
Other font styles liked:
• Up to you

Requirements
Must have
• All contact info. The design is up to you.
Nice to have
• All the contact info the design is up to you
Should not have
• I don't have any

```html
<!DOCTYPE html>
<html lang="en">
<head>
<meta charset="utf-8">
<title>Summit Grading And Builders – Business Card</title>
<link rel="stylesheet" href="https://fonts.googleapis.com/css2?family=Cinzel:wght@400;500&family=EB+Garamond:wght@400&display=swap">
<style>
  :root{
    --backdrop:#3b3140;
    --card:#ffffff;
    --ink:#15161f;
    --band:#161826;
    --band-edge:#24283a;
    --accent:#1aa3ec;
    --accent-deep:#0a5fb0;
    --light-text:#f2f4f8;
  }
  *{margin:0;padding:0;box-sizing:border-box}
  html,body{width:1200px;height:800px;overflow:hidden;background:var(--backdrop)}
  .canvas{position:relative;width:1200px;height:800px}
  .card{position:absolute;top:245px;width:540px;height:309px;background:var(--card);overflow:hidden;box-shadow:0 12px 30px rgba(0,0,0,.35)}
  .card--front{left:40px}
  .card--back{left:620px}

  .band{position:absolute;left:0;right:0;background:linear-gradient(90deg,var(--band) 0%,var(--band-edge) 100%)}
  .card--front .band{top:196px;bottom:0}
  .card--back .band{top:118px;height:146px;border-top:3px solid var(--accent);border-bottom:3px solid var(--accent-deep)}

  .brand{position:absolute;display:flex;align-items:center;gap:10px;font-family:"Cinzel",serif;font-weight:400;color:var(--ink);letter-spacing:.02em;white-space:nowrap}
  .brand__mark{display:block;background:var(--accent)}
  .card--front .brand{left:0;right:0;top:90px;justify-content:center;font-size:22px}
  .card--front .brand__mark{width:18px;height:18px}
  .card--back .brand{right:22px;top:88px;font-size:9px;gap:6px}
  .card--back .brand__mark{width:9px;height:9px}

  .contact{position:absolute;list-style:none;font-family:"EB Garamond",serif;color:var(--light-text)}
  .contact li{display:flex;align-items:center;gap:10px;white-space:nowrap}
  .icon{width:20px;height:20px;flex:none}
  .card--front .contact--phones{left:24px;top:212px;font-size:15px}
  .card--front .contact--phones li{margin-bottom:8px}
  .card--front .contact--online{right:26px;top:238px;font-size:14px}
  .card--front .contact--online li{margin-bottom:8px}
  .card--back .contact{left:34px;top:134px;font-size:15px}
  .card--back .contact li{margin-bottom:8px}

  .owner{position:absolute;left:30px;top:24px;color:var(--ink)}
  .owner__name{font-family:"Cinzel",serif;font-weight:500;font-size:30px;letter-spacing:.01em;line-height:1}
  .owner__title{font-family:"Cinzel",serif;font-size:19px;margin-top:6px;line-height:1}
  .owner__company{font-family:"Cinzel",serif;font-size:8px;margin-top:4px;letter-spacing:.02em}
</style>
</head>
<body>
<svg width="0" height="0" style="position:absolute" aria-hidden="true">
  <defs>
    <symbol id="icon-phone" viewBox="0 0 20 20">
      <circle cx="10" cy="10" r="10" fill="#1aa3ec"/>
      <path d="M7 5.5c.6-.3 1.1 0 1.3.5l.6 1.5c.2.5 0 .9-.4 1.1l-.5.3c.4 1 1.2 1.9 2.2 2.4l.4-.5c.3-.4.7-.5 1.1-.3l1.5.7c.5.2.7.8.4 1.3-.5.9-1.5 1.4-2.5 1.1C8.6 12.9 6.5 10.6 6 8c-.2-1 .2-2 1-2.5z" fill="#fff"/>
    </symbol>
    <symbol id="icon-fax" viewBox="0 0 20 20">
      <circle cx="10" cy="10" r="10" fill="#1aa3ec"/>
      <rect x="7" y="4.5" width="6" height="3.5" fill="#fff"/>
      <rect x="4.5" y="8" width="11" height="5" rx="1" fill="#fff"/>
      <rect x="7" y="12" width="6" height="3.5" fill="#fff" stroke="#1aa3ec" stroke-width=".8"/>
    </symbol>
    <symbol id="icon-mail" viewBox="0 0 20 20">
      <circle cx="10" cy="10" r="10" fill="#1aa3ec"/>
      <rect x="5" y="6.5" width="10" height="7" fill="#fff"/>
      <path d="M5 6.5l5 4 5-4" fill="none" stroke="#1aa3ec" stroke-width="1"/>
    </symbol>
    <symbol id="icon-web" viewBox="0 0 20 20">
      <circle cx="10" cy="10" r="10" fill="#1aa3ec"/>
      <circle cx="10" cy="10" r="5.5" fill="none" stroke="#fff" stroke-width="1.2"/>
      <ellipse cx="10" cy="10" rx="2.3" ry="5.5" fill="none" stroke="#fff" stroke-width="1"/>
      <path d="M4.5 10h11M5.3 7.5h9.4M5.3 12.5h9.4" stroke="#fff" stroke-width="1"/>
    </symbol>
  </defs>
</svg>

<main class="canvas">
  <section class="card card--front" aria-label="Business card front">
    <div class="brand"><span class="brand__mark"></span>Summit Grading And Builders</div>
    <div class="band"></div>
    <ul class="contact contact--phones">
      <li><svg class="icon"><use href="#icon-phone"/></svg>555-214-7390</li>
      <li><svg class="icon"><use href="#icon-fax"/></svg>555-806-3127</li>
    </ul>
    <ul class="contact contact--online">
      <li><svg class="icon"><use href="#icon-mail"/></svg>summitgradingandbuilders@mailbox.example</li>
      <li><svg class="icon"><use href="#icon-web"/></svg>www.summitgradingandbuilders.example</li>
    </ul>
  </section>

  <section class="card card--back" aria-label="Business card back">
    <div class="owner">
      <p class="owner__name">Martin Kowalczyk</p>
      <p class="owner__title">Owner</p>
      <p class="owner__company">Summit Grading And Builders</p>
    </div>
    <div class="brand"><span class="brand__mark"></span>Summit Grading And Builders</div>
    <div class="band"></div>
    <ul class="contact">
      <li><svg class="icon"><use href="#icon-phone"/></svg>555-214-7390</li>
      <li><svg class="icon"><use href="#icon-fax"/></svg>555-806-3127</li>
      <li><svg class="icon"><use href="#icon-mail"/></svg>summitgradingandbuilders@mailbox.example</li>
      <li><svg class="icon"><use href="#icon-web"/></svg>www.summitgradingandbuilders.example</li>
    </ul>
  </section>
</main>
</body>
</html>
```